Birch Polar Methods Consulting Company Template

Microsoft Word template for a professional retail consulting company that can suggestingly mimic the attached design, but in vertical fashion - . Important - It doesn't have to mimic this design. I accept creativity, professionalism, and eye catching work!

I'd also like suggestingly the globe of the attached logo to appear as an imprint in the background

To win the contest, please make it look extremely impressive, attention grabbing, and don't fear giving it your own creative unique design elements.

The Word template is needed for me to create Word documents from, so it is highly important that I would be able to write memos in Word, and for those same memos to look clean.

Target Market(s)

Retailers interested in consulting services from Birch Toolworks

Font styles to use
Serif

Requirements
Must have
• Birch Polar Methods logo represented. Also, red and black logo colors. A professional, modern, outstanding look and design. Must be somewhat bold and upmarket.
Nice to have
• I accept all forms of creativity.
Should not have
• Cartoon / child looking

```html
<!DOCTYPE html>
<html lang="en">
<head>
<meta charset="utf-8">
<title>Birch Polar Methods – Document Template</title>
<link rel="stylesheet" href="https://fonts.googleapis.com/css2?family=Fira+Sans:wght@400;500;600&family=Fira+Sans+Condensed:wght@300;400;600&family=Oswald:wght@300&family=PT+Serif&display=swap">
<style>
  :root {
    --red: #f0062a;
    --red-deep: #c8001e;
    --pink: #f9a7b4;
    --ink: #1e1e22;
    --text: #2b2b2b;
    --rule: #3a3a3a;
    --canvas: #d9e0e0;
    --paper: #ffffff;
  }
  * { box-sizing: border-box; margin: 0; padding: 0; }
  html, body { width: 1200px; height: 1200px; overflow: hidden; }
  body { background: var(--canvas); font-family: "Fira Sans", sans-serif; position: relative; }

  .page { position: absolute; background: var(--paper); overflow: hidden; }
  .page svg.art { position: absolute; inset: 0; }

  .imprint {
    position: absolute; border-radius: 50%;
    background: radial-gradient(circle, rgba(240,6,42,0.06) 0%, rgba(240,6,42,0.05) 55%, rgba(240,6,42,0) 72%);
  }

  /* brand lockup */
  .brand { position: absolute; display: flex; align-items: center; gap: 12px; }
  .brand-dot { border-radius: 50%; background: var(--red); flex: none; }
  .brand-name {
    font-family: "Fira Sans Condensed", sans-serif; font-weight: 600;
    color: var(--ink); letter-spacing: 0.5px; line-height: 1; white-space: nowrap;
  }
  .brand-tagline {
    font-family: "Fira Sans", sans-serif; font-weight: 500; color: var(--red);
    letter-spacing: 1.4px; white-space: nowrap; margin-top: 6px;
  }

  /* cover page */
  .cover { left: 46px; top: 182px; width: 605px; height: 852px; }
  .cover .brand { left: 32px; top: 44px; }
  .cover .brand-dot { width: 76px; height: 76px; }
  .cover .brand-name { font-size: 36px; }
  .cover .brand-tagline { font-size: 13.5px; letter-spacing: 2.4px; }
  .cover .rule {
    position: absolute; left: 32px; top: 140px; width: 540px; height: 2px;
    background: linear-gradient(90deg, var(--rule) 0 51%, var(--red) 51% 100%);
  }
  .doc-title {
    position: absolute; left: 30px; top: 162px;
    font-family: "Fira Sans Condensed", sans-serif; font-weight: 300;
    font-size: 70px; letter-spacing: 3.4px; color: var(--red); white-space: nowrap;
  }
  .doc-subtitle {
    position: absolute; left: 33px; top: 248px;
    font-family: "Oswald", sans-serif; font-weight: 300; font-size: 32px;
    letter-spacing: 2.6px; color: var(--ink); white-space: nowrap;
  }
  .doc-body {
    position: absolute; left: 33px; top: 309px; width: 527px;
    font-family: "Fira Sans Condensed", sans-serif; font-size: 13px;
    line-height: 27.3px; color: var(--text); text-align: justify;
  }
  .doc-body p + p { margin-top: 16px; }
  .visit {
    position: absolute; left: 21px; top: 786px;
    font-family: "Fira Sans", sans-serif; font-size: 20px; line-height: 29px;
    color: var(--red-deep); letter-spacing: 0.8px;
  }

  /* contents page */
  .contents { left: 704px; top: 38px; width: 383px; height: 541px; }
  .contents-head {
    position: absolute; left: 20px; top: 24px;
    font-family: "Fira Sans", sans-serif; font-weight: 600; font-size: 11px;
    letter-spacing: 1.3px; color: #fff;
  }
  .contents-num { position: absolute; right: 22px; top: 24px; font-size: 11px; color: #fff; font-weight: 500; }
  .contents .brand { left: 222px; top: 24px; gap: 4px; }
  .contents .brand-dot { width: 12px; height: 12px; }
  .contents .brand-name { font-size: 6px; letter-spacing: 0.3px; }
  .toc { position: absolute; left: 23px; top: 67px; width: 335px; list-style: none; }
  .toc li {
    display: flex; align-items: baseline; height: 18.7px;
    font-family: "PT Serif", serif; font-size: 8.5px; color: var(--ink);
  }
  .toc li.gap { margin-top: 4px; }
  .toc .leader { flex: 1; border-bottom: 1px dotted #555; margin: 0 40px 0 3px; }
  .contents-url {
    position: absolute; right: 16px; bottom: 12px;
    font-family: "Fira Sans", sans-serif; font-weight: 600; font-size: 9px;
    letter-spacing: 0.5px; color: #fff;
  }

  /* back page */
  .back { left: 709px; top: 610px; width: 375px; height: 528px; }
  .back .brand { left: 20px; top: 42px; gap: 9px; }
  .back .brand-dot { width: 58px; height: 58px; }
  .back .brand-name { font-size: 25px; }
  .back .brand-tagline { font-size: 10px; margin-top: 4px; letter-spacing: 1.8px; }
  .back .rule { position: absolute; left: 22px; top: 121px; width: 298px; height: 1px; background: #777; }
  .back-heading {
    position: absolute; left: 26px; top: 130px;
    font-family: "Fira Sans", sans-serif; font-weight: 400; font-size: 24px; line-height: 35px;
    letter-spacing: 1.4px; color: var(--red);
  }
  .contact { position: absolute; left: 19px; top: 420px; list-style: none; color: var(--red-deep); }
  .contact li {
    display: flex; align-items: flex-start; gap: 7px;
    font-family: "Fira Sans", sans-serif; font-weight: 500; font-size: 11px; line-height: 15.5px;
  }
  .contact li.space { margin-top: 10px; }
  .contact svg { width: 9px; height: 9px; margin-top: 3px; flex: none; fill: var(--red-deep); }
</style>
</head>
<body>

<!-- Cover / memo page -->
<section class="page cover">
  <div class="imprint" role="img" aria-label="Faint background imprint of the brand emblem" style="left:20px;top:330px;width:470px;height:420px;"></div>
  <svg class="art" width="605" height="852" viewBox="0 0 605 852">
    <defs>
      <linearGradient id="pinkFade1" x1="0" y1="0" x2="0" y2="1">
        <stop offset="0" stop-color="#fde6ea"/>
        <stop offset="1" stop-color="#f98d9e"/>
      </linearGradient>
    </defs>
    <polygon points="489,633 326,852 530,852" fill="url(#pinkFade1)"/>
    <path d="M605,440 L500,580 Q492,592 494,608 L532,852 L605,852 Z" fill="var(--red)"/>
  </svg>

  <div class="brand">
    <span class="brand-dot"></span>
    <div>
      <div class="brand-name">BIRCH POLAR METHODS</div>
      <div class="brand-tagline">ADVISE | ALIGN | ADVANCE</div>
    </div>
  </div>
  <div class="rule"></div>
  <h1 class="doc-title">YOUR TITLE HERE</h1>
  <h2 class="doc-subtitle">YOUR SUB TITLE HERE</h2>
  <div class="doc-body">
    <p>Lorem Ipsum is simply dummy text of the printing and typesetting industry. Lorem Ipsum has been the industry's standard dummy text ever since the 1500s, when an unknown printer took a galley of type and scrambled it to make a type specimen book. It has survived not only five centuries.</p>
    <p>But also the leap into electronic typesetting, remaining essentially unchanged. It was popularised in the 1960s with the release of Letraset sheets containing Lorem Ipsum passages, and more recently with desktop publishing software like Aldus Page Maker including versions of Lorem Ipsum time.</p>
  </div>
  <div class="visit">Visit us<br>www.birchpolarmethods.com</div>
</section>

<!-- Table of contents page -->
<section class="page contents">
  <div class="imprint" role="img" aria-label="Faint background imprint of the brand emblem" style="left:60px;top:110px;width:290px;height:330px;"></div>
  <svg class="art" width="383" height="541" viewBox="0 0 383 541">
    <polygon points="0,22 220,22 212,38 0,38" fill="var(--red)"/>
    <polygon points="318,22 383,22 383,38 310,38" fill="var(--red)"/>
    <path d="M0,518 C90,520 150,505 220,480 C290,456 345,448 383,458 L383,541 L0,541 Z" fill="var(--red)"/>
    <path d="M0,514 C90,516 150,500 220,475 C290,451 345,443 383,453" fill="none" stroke="#3a0a10" stroke-width="3"/>
    <path d="M0,522 C90,524 150,509 220,484 C290,460 345,452 383,462" fill="none" stroke="#fff" stroke-width="1.5"/>
  </svg>
  <div class="contents-head">Table Of Contents</div>
  <div class="brand"><span class="brand-dot"></span><span class="brand-name">BIRCH POLAR METHODS</span></div>
  <div class="contents-num">02</div>
  <ul class="toc">
    <li>Lorem Ipsum<span class="leader"></span>1</li>
    <li>Lorem Ipsum<span class="leader"></span>3</li>
    <li>Lorem Ipsum<span class="leader"></span>3</li>
    <li>Lorem Ipsum<span class="leader"></span>3</li>
    <li>Lorem Ipsum<span class="leader"></span>4</li>
    <li>Lorem Ipsum<span class="leader"></span>4</li>
    <li>Lorem Ipsum<span class="leader"></span>4</li>
    <li class="gap">Lorem Ipsum<span class="leader"></span>5</li>
    <li>Lorem Ipsum<span class="leader"></span>5</li>
    <li>Lorem Ipsum<span class="leader"></span>6</li>
    <li>Lorem Ipsum<span class="leader"></span>6</li>
    <li>Lorem Ipsum<span class="leader"></span>6</li>
    <li>Lorem Ipsum<span class="leader"></span>7</li>
    <li>Lorem Ipsum<span class="leader"></span>7</li>
  </ul>
  <div class="contents-url">www.birchpolarmethods.com</div>
</section>

<!-- Back cover -->
<section class="page back">
  <svg class="art" width="375" height="528" viewBox="0 0 375 528">
    <defs>
      <linearGradient id="pinkFade2" x1="0" y1="0" x2="0" y2="1">
        <stop offset="0" stop-color="#fde6ea"/>
        <stop offset="1" stop-color="#f98d9e"/>
      </linearGradient>
      <linearGradient id="whiteWash" x1="0" y1="0" x2="0" y2="1">
        <stop offset="0.45" stop-color="#fff"/>
        <stop offset="1" stop-color="#fdeef0"/>
      </linearGradient>
    </defs>
    <rect width="375" height="528" fill="url(#whiteWash)"/>
    <polygon points="302,415 202,528 336,528" fill="url(#pinkFade2)"/>
    <path d="M375,272 L310,358 Q304,367 306,378 L336,528 L375,528 Z" fill="var(--red)"/>
  </svg>
  <div class="brand">
    <span class="brand-dot"></span>
    <div>
      <div class="brand-name">BIRCH POLAR METHODS</div>
      <div class="brand-tagline">ADVISE | ALIGN | ADVANCE</div>
    </div>
  </div>
  <div class="rule"></div>
  <h2 class="back-heading">GLOBAL<br>CONSULTING COMPANY</h2>
  <ul class="contact">
    <li><svg viewBox="0 0 10 10"><path d="M5 0a3.5 3.5 0 0 1 3.5 3.5C8.5 6 5 10 5 10S1.5 6 1.5 3.5A3.5 3.5 0 0 1 5 0zm0 2a1.5 1.5 0 1 0 0 3 1.5 1.5 0 0 0 0-3z"/></svg><span>Dummy City<br>Dummy Country, Land</span></li>
    <li class="space"><svg viewBox="0 0 10 10"><path d="M2 0l2 2.5-1 1.2c.6 1.3 1.6 2.3 2.9 2.9l1.2-1L10 8 8.6 9.8C4.3 9.8.2 5.7.2 1.4z"/></svg><span>1-555-010-2040</span></li>
    <li><svg viewBox="0 0 10 10"><path d="M5 0a5 5 0 1 0 0 10A5 5 0 0 0 5 0zm0 1.3a3.7 3.7 0 1 1 0 7.4 3.7 3.7 0 0 1 0-7.4z"/></svg><span>www.birchpolarmethods.com</span></li>
    <li><svg viewBox="0 0 10 10"><path d="M0 2h10v6H0zM0 2l5 3.5L10 2" stroke="#fff" stroke-width=".8"/></svg><span>nora@birchpolarmethods.com</span></li>
  </ul>
</section>

</body>
</html>
```